BPRV Postcard Design: Mosquito Control, Lawn Maintenance and Pressure washing

I have a new company based in Atlanta,Georgia named Brightwell Pest Relief Ventures, LLC. We specializes in Mosquito Control. We also have additional services: Lawn maintenance, Pressure Washing and Gutter Cleaning. I would like to see designs with the colors Black, Red, Gray. We would like the customer to think of us when it comes to Enjoying a mosquito free yard and improving the look and feel of their home and lawn.

Industry/Entity Type

It Company

Requirements
Nice to have
• Treatment plans starting at $69/mt - front of card
• The additional services we offer - back of card.

```html
<!DOCTYPE html>
<html lang="en">
<head>
<meta charset="utf-8">
<title>Brightwell Pest Relief Ventures, LLC — Postcard</title>
<link rel="stylesheet" href="https://fonts.googleapis.com/css2?family=Michroma&family=Ubuntu:ital,wght@1,700&family=Source+Code+Pro:wght@500&display=swap">
<style>
  :root {
    --red: #ec2024;
    --black: #000000;
    --gray: #8a8585;
    --gray-light: #d9d6d6;
    --mascot-light: #e2cfe3;
    --mascot-warm: #c99a4a;
  }
  html, body {
    margin: 0;
    padding: 0;
    width: 1200px;
    height: 1000px;
    overflow: hidden;
    background: var(--black);
  }
  .postcard {
    display: block;
    width: 1200px;
    height: 1000px;
  }
  .panel-red { fill: var(--red); }
  .brand-name {
    font-family: "Michroma", sans-serif;
    font-size: 84px;
    fill: var(--gray);
  }
  .brand-rule {
    fill: var(--gray);
    stroke: var(--gray-light);
    stroke-width: 2;
  }
  .brand-tagline {
    font-family: "Ubuntu", sans-serif;
    font-style: italic;
    font-weight: 700;
    font-size: 46px;
    fill: var(--black);
  }
  .phone-box { fill: var(--black); }
  .phone-number {
    font-family: "Source Code Pro", monospace;
    font-weight: 500;
    font-size: 72px;
    fill: var(--red);
  }
</style>
</head>
<body>
<svg class="postcard" viewBox="0 0 1200 1000" xmlns="http://www.w3.org/2000/svg">
  <defs>
    <linearGradient id="mascotTone" x1="0" y1="0" x2="1" y2="1">
      <stop offset="0" stop-color="var(--mascot-light)"/>
      <stop offset="0.6" stop-color="var(--mascot-light)"/>
      <stop offset="1" stop-color="var(--mascot-warm)"/>
    </linearGradient>
  </defs>

  <!-- background panels split by the diagonal band -->
  <polygon class="panel-red" points="0,0 950,0 160,1000 0,1000"/>
  <polygon class="panel-red" points="930,105 1150,105 1150,1000 245,1000"/>

  <!-- mascot illustration area -->
  <rect class="mascot" x="55" y="95" width="425" height="650" rx="60"
        fill="url(#mascotTone)" role="img"
        aria-label="Cartoon dragonfly mascot with lavender wings and a brown and yellow body, flying toward the left"/>

  <!-- brand lockup -->
  <text class="brand-name" x="608" y="655" textLength="522" lengthAdjust="spacingAndGlyphs">BRIGHTWELL</text>
  <rect class="brand-rule" x="606" y="670" width="530" height="15" rx="4"/>
  <text class="brand-tagline" x="505" y="750" textLength="635" lengthAdjust="spacingAndGlyphs">Pest Relief Ventures LLC</text>

  <!-- phone -->
  <rect class="phone-box" x="543" y="784" width="555" height="91"/>
  <text class="phone-number" x="820" y="856" text-anchor="middle" textLength="490" lengthAdjust="spacingAndGlyphs">404-555-0192</text>
</svg>
</body>
</html>
```